Brightnest Stays Stationery Design

Letterpaper, business cards, notebook, envelope A4 & A5

Target Market(s)

Business, accommodation, hotels, flexible housing

Font styles to use
Other font styles liked:
• Montserrat

Colors

Designer to choose only greyscale colors for use in the design.

Requirements
Must have
• Luxurious appearance
Keep it simple, just like the logo
Modern
Nice to have
• Tight Luxury Design
Should not have
• Illustrations
Decorative

```html
<!DOCTYPE html>
<html lang="en">
<head>
<meta charset="utf-8">
<title>Brightnest Stays Stationery</title>
<link rel="stylesheet" href="https://fonts.googleapis.com/css2?family=Montserrat:wght@400;500;600&display=swap">
<style>
:root{
  --ink:#1c1c1e;
  --ink-soft:#4a4a4d;
  --grey-text:#8a8a8e;
  --paper:#ffffff;
  --dark:#1e1e20;
  --bg-top:#efeff0;
  --bg-mid:#d4d4d6;
  --bg-bottom:#d9d9db;
  --shadow:rgba(0,0,0,.28);
}
*{margin:0;padding:0;box-sizing:border-box}
html,body{width:1200px;height:3434px;overflow:hidden}
body{font-family:"Montserrat",sans-serif;color:var(--ink);position:relative;background:var(--bg-top)}
.section{position:absolute;left:0;width:1200px}
.section--overview{top:0;height:787px;background:var(--bg-top)}
.section--formats{top:787px;height:1396px;background:var(--bg-mid)}
.section--letterhead{top:2183px;height:1251px;background:var(--bg-bottom)}
.sheet{position:absolute;background:var(--paper);box-shadow:4px 6px 10px var(--shadow)}

/* brand wordmark */
.brand{display:flex;flex-direction:column;align-items:center;color:var(--ink)}
.brand__square{border:1.5px solid currentColor}
.brand__name{font-weight:500;text-transform:uppercase;white-space:nowrap;line-height:1}

/* overview items */
.letter{left:296px;top:88px;width:293px;height:416px;padding:26px 26px 14px}
.letter .brand__square{width:20px;height:20px}
.letter .brand__name{font-size:7px;letter-spacing:1px;margin-top:5px}
.letter__body{margin-top:30px;font-size:4.6px;line-height:1.55;color:var(--ink-soft)}
.letter__body p{margin-bottom:7px}
.letter__footer{position:absolute;left:0;right:0;bottom:12px;text-align:center;font-size:4.6px;color:var(--ink-soft);line-height:1.7}

.folder{left:640px;top:69px;width:347px;height:438px;background:var(--dark)}
.folder .brand{position:absolute;left:0;right:0;top:134px;color:#f2f2f2}
.folder .brand__square{width:88px;height:100px}
.folder .brand__name{font-size:21px;letter-spacing:3px;margin-top:22px;font-weight:400}
.folder__band{position:absolute;left:0;right:0;top:400px;height:16px;background:#e6e6e6;text-align:center;font-size:8px;font-weight:600;letter-spacing:.8px;line-height:16px;color:var(--ink-soft)}

.card{left:191px;top:541px;width:132px;height:72px;padding:8px}
.card .brand{position:absolute;right:10px;top:8px}
.card .brand__square{width:12px;height:13px}
.card .brand__name{font-size:4.5px;letter-spacing:.5px;margin-top:3px}
.card__rule{position:absolute;left:8px;right:8px;top:40px;border-top:.8px solid #bbb}
.card__person{position:absolute;left:8px;top:33px;font-size:4.3px;font-weight:600;text-transform:uppercase}
.card__role{display:block;font-weight:400;text-transform:none;color:var(--grey-text);margin-top:1px}
.card__contact{position:absolute;left:8px;top:50px;font-size:3.6px;line-height:1.5;color:var(--ink-soft)}
.card__address{position:absolute;right:8px;top:52px;font-size:3.6px;line-height:1.5;text-align:right;color:var(--ink-soft)}
.card-back{left:191px;top:637px;width:132px;height:74px;background:#2b2b2d}

.envelope-front{left:357px;top:551px;width:330px;height:156px;padding:22px 0 0 24px}
.envelope-front .brand{width:74px}
.envelope-front .brand__square{width:20px;height:21px}
.envelope-front .brand__name{font-size:6px;letter-spacing:.6px;margin-top:5px}
.envelope-front__address{width:74px;text-align:center;font-size:5.4px;line-height:1.3;color:var(--ink-soft);margin-top:2px}
.envelope-back{left:717px;top:551px;width:328px;height:156px}
.envelope-back .brand{position:absolute;left:0;right:0;top:15px}
.envelope-back .brand__name{font-size:11px;letter-spacing:1.2px;font-weight:400}

/* format mockups */
.flap{position:absolute;left:0;top:0;width:100%;background:var(--paper);
  clip-path:polygon(0 0,100% 0,98.5% 40%,97% 100%,3% 100%,1.5% 40%)}
.flap-wrap{position:absolute;left:0;top:0;width:100%;filter:drop-shadow(0 5px 4px rgba(0,0,0,.25))}
.flap .brand{position:absolute;left:0;right:0;top:22px}
.flap .brand__name{font-size:15px;letter-spacing:1.4px;font-weight:600}

.front-mark{position:absolute;left:15px;top:40px;width:130px}
.front-mark .brand__square{width:40px;height:43px}
.front-mark .brand__name{font-size:10px;letter-spacing:.8px;font-weight:600;margin-top:9px}
.front-mark__address{text-align:center;font-size:9px;line-height:1.3;color:var(--grey-text);margin-top:4px;font-weight:500}

.fmt-a4-front{left:147px;top:129px;width:440px;height:620px}
.fmt-a4-back{left:623px;top:129px;width:438px;height:620px}
.fmt-a4-back .flap{height:77px}
.fmt-a5-front{left:147px;top:777px;width:441px;height:313px}
.fmt-a5-back{left:621px;top:777px;width:440px;height:313px}
.fmt-a5-back .flap{height:76px}
.fmt-dl-front{left:147px;top:1113px;width:441px;height:205px}
.fmt-dl-front .front-mark{left:6px;top:26px;width:110px}
.fmt-dl-front .brand__square{width:30px;height:33px}
.fmt-dl-front .brand__name{font-size:8.5px;margin-top:6px}
.fmt-dl-front .front-mark__address{font-size:7.5px}
.fmt-dl-back{left:621px;top:1113px;width:440px;height:205px}
.fmt-dl-back .flap{height:75px}

/* single letterhead */
.letterhead{left:228px;top:172px;width:645px;height:898px;box-shadow:0 10px 24px rgba(0,0,0,.18)}
.letterhead .letterhead-mark{position:absolute;right:26px;top:61px;width:200px}
.letterhead-mark .brand__square{width:60px;height:70px}
.letterhead-mark .brand__name{font-size:16px;letter-spacing:2.4px;font-weight:400;margin-top:20px}
</style>
</head>
<body>

<section class="section section--overview">
  <article class="sheet letter">
    <div class="brand"><span class="brand__square"></span><span class="brand__name">Brightnest Stays</span></div>
    <div class="letter__body">
      <p>Dear customer,</p>
      <p>Thank you for choosing our flexible rooms for your upcoming stay. Every apartment is fully furnished, cleaned weekly and ready the moment you arrive, so you can settle in without any worries.</p>
      <p>Our team is available day and night to help with check-in, extra services or any questions about your booking. We look forward to welcoming you and making your stay comfortable.</p>
      <p>Long stays receive a reduced monthly rate, and business guests can request invoices on company name. Simply reply to this letter or contact our office to arrange the details.</p>
      <p>We hope to see you soon.</p>
      <p>Kind regards,</p>
    </div>
    <div class="letter__footer">
      Lindenlaan 14, 4811 AB Breda<br>
      +31 20 555 0147 &nbsp;·&nbsp; info@brightnest.nl &nbsp;·&nbsp; www.brightnest.nl
    </div>
  </article>

  <article class="sheet folder">
    <div class="brand"><span class="brand__square"></span><span class="brand__name">Brightnest Stays</span></div>
    <div class="folder__band">www.brightnest.nl</div>
  </article>

  <article class="sheet card">
    <div class="brand"><span class="brand__square"></span><span class="brand__name">Brightnest Stays</span></div>
    <div class="card__person">Sanne Vermeer<span class="card__role">Managing Director</span></div>
    <div class="card__rule"></div>
    <div class="card__contact">+31 20 555 0147<br>info@brightnest.nl<br>www.brightnest.nl</div>
    <div class="card__address">Lindenlaan 14,<br>4811 AB Breda</div>
  </article>
  <div class="sheet card-back" role="img" aria-label="Business card reverse with a dark repeating brand pattern"></div>

  <article class="sheet envelope-front">
    <div class="brand"><span class="brand__square"></span><span class="brand__name">Brightnest Stays</span></div>
    <div class="envelope-front__address">Lindenlaan 14,<br>4811 AB Breda</div>
  </article>
  <article class="sheet envelope-back">
    <div class="brand"><span class="brand__name">Brightnest Stays</span></div>
  </article>
</section>

<section class="section section--formats">
  <article class="sheet fmt-a4-front">
    <div class="brand front-mark"><span class="brand__square"></span><span class="brand__name">Brightnest Stays</span><div class="front-mark__address">Lindenlaan 14,<br>4811 AB Breda</div></div>
  </article>
  <article class="sheet fmt-a4-back">
    <div class="flap-wrap"><div class="flap"><div class="brand"><span class="brand__name">Brightnest Stays</span></div></div></div>
  </article>

  <article class="sheet fmt-a5-front">
    <div class="brand front-mark"><span class="brand__square"></span><span class="brand__name">Brightnest Stays</span><div class="front-mark__address">Lindenlaan 14,<br>4811 AB Breda</div></div>
  </article>
  <article class="sheet fmt-a5-back">
    <div class="flap-wrap"><div class="flap"><div class="brand"><span class="brand__name">Brightnest Stays</span></div></div></div>
  </article>

  <article class="sheet fmt-dl-front">
    <div class="brand front-mark"><span class="brand__square"></span><span class="brand__name">Brightnest Stays</span><div class="front-mark__address">Lindenlaan 14,<br>4811 AB Breda</div></div>
  </article>
  <article class="sheet fmt-dl-back">
    <div class="flap-wrap"><div class="flap"><div class="brand"><span class="brand__name">Brightnest Stays</span></div></div></div>
  </article>
</section>

<section class="section section--letterhead">
  <article class="sheet letterhead">
    <div class="brand letterhead-mark"><span class="brand__square"></span><span class="brand__name">Brightnest Stays</span></div>
  </article>
</section>

</body>
</html>
```